Verpackungsaufkleber kreieren für Kaninchenheu
Zielgruppe
Wir ernten und vertreiben hochwertiges Futter (insbesondere Heu/Stroh) für Kaninchen und alle Heimtiere. Wir vertreiben derzeit unsere Produkte vorranging über unseren Online-Shop (www.strohkörbchen.de). Da wir uns der ökologischen und naturverbundenen Verpackung verbunden haben, möchten wir die Papier-Verpackung entsprechend hochwertig und ansprechend in die Regale der Einzelhändler zum Verkauf anbieten. Unsere Zielgruppe im Onlineshop sind meist Frauen, 16-50 J., welche besonderen Wert auf Qualität und ansprechende Verpackung legen.
Aufgabenstellung
Wir haben uns zu dem Design überlegt, dass es toll wäre, wenn der Kunde unsere Heu-Produkte in einer Papierverpackung in den Regalen sieht und ein Label in Form eines 'durchsichtigen Fensters' auf der Verpackung klebt, welches imitiert, dass es einen tatsächlichen Einblick in die Papiertüte auf das hochwertige Heu gewährt.
Also dass der Kunde den Eindruck hat, dass Heu in Form eines Fensters zu sehen. Dabei soll jedoch auch unser aktuelles Logo am Rand miteingebunden werden, sowie einen Textbereich mit ein paar Informationen zum Heu. Sofern Kapazitäten und interessante Neugestaltung des Logos eingebracht werden können würden wir auch hierbei überlegen unser aktuelles Logo auszuwechseln.
Die weitere Überlegung wäre, einen Aufkleber für beide Verpackungsvarianten (Papiertüten und Plastiktüten) zu kreieren . Hierzu gibt es keine Überlegungen unserseits. Dies würde den Vorteil mit sich bringen, dass wir nur eine Vorlage als Aufkleber drucken müssen. D.h. der oben beschriebenen Vorschlag dient hauptsächlich dazu, dass der Kunde eine Vorstellung hat, welches Produkt sich darin befindet, wobei man bei der durchsichtigen Plastiktüte das Produkt natürlich sehen kann und hierbei das Heu als Bild nicht zwingend in diesem Sichtfenster vollflächig dargestellt werden müsste.
Als Idee könnte man auch noch die regionale Eifellandschaft mit einbinden.
Diese Ausgestaltung möchten wir aber Euch und Euren kreativen Köpfen überlassen.
Wir freuen uns über interessante Vorschläge!

```html
<!DOCTYPE html>
<html lang="de">
<head>
<meta charset="utf-8">
<title>Strohkörbchen – Heu-Etikett</title>
<link href="https://fonts.googleapis.com/css2?family=Arimo:wght@400;700&display=swap" rel="stylesheet">
<style>
  :root {
    --backdrop: #4a4a4a;
    --cream: #f5f1a9;
    --tan: #b39f6c;
    --tan-text: #f7efc4;
    --green: #84c318;
    --ink: #1e1e1e;
    --white: #ffffff;
  }
  * { box-sizing: border-box; margin: 0; padding: 0; }
  html, body { width: 729px; height: 1200px; overflow: hidden; }
  body {
    background: var(--backdrop);
    font-family: "Arimo", Arial, sans-serif;
    color: var(--ink);
    position: relative;
  }
  .label {
    position: absolute;
    left: 47px; top: 151px;
    width: 634px; height: 898px;
    background: var(--cream);
    overflow: hidden;
  }
  .landscape {
    position: absolute; left: 0; top: 0;
    width: 634px; height: 340px;
    background: linear-gradient(180deg, #5f6670 0%, #8e949a 22%, #a9b06a 40%, #8da33a 55%, #5f7a25 75%, #3f5619 100%);
  }
  .hay-window {
    position: absolute; left: 42px; top: 183px;
    width: 355px; height: 150px;
    border-radius: 40px 70px 20px 40px;
    background: linear-gradient(135deg, #a8ac84, #8f9a6a 50%, #b8b590);
    border: 5px solid var(--tan);
  }
  .rabbits {
    position: absolute; left: 408px; top: 240px;
    width: 190px; height: 95px;
    border-radius: 8px;
    background: linear-gradient(90deg, #d9d2c6, #c9b9a3 60%, #b3865a);
  }
  .brand-name {
    position: absolute; left: 63px; top: 164px;
    font-size: 20px; font-weight: 400;
    color: var(--white);
    letter-spacing: 0.3px;
  }
  .green-band {
    position: absolute; left: 0; top: 340px;
    width: 634px; height: 20px;
    background: var(--green);
  }
  .benefits-title {
    position: absolute; left: 43px; top: 386px;
    width: 547px; height: 52px;
    background: var(--tan);
    color: var(--tan-text);
    font-weight: 700; font-size: 15.5px; line-height: 20px;
    padding: 6px 0 0 21px;
  }
  .benefits {
    position: absolute; left: 52px; top: 446px;
    list-style: none;
    font-size: 17px; line-height: 20.3px;
  }
  .benefits li { position: relative; padding-left: 33px; }
  .benefits svg { position: absolute; left: 0; top: 3px; width: 16px; height: 15px; }
  .analysis-title {
    position: absolute; left: 43px; top: 646px;
    width: 547px; height: 30px;
    background: var(--tan);
    color: var(--tan-text);
    font-weight: 700; font-size: 20px;
    text-align: center; line-height: 30px;
  }
  .analysis {
    position: absolute; left: 45px; top: 684px;
    display: flex; gap: 4px;
  }
  .analysis-cell {
    height: 72px;
    background: var(--tan);
    color: var(--tan-text);
    text-align: center;
    font-size: 18px;
    padding-top: 9px;
  }
  .analysis-cell .value { display: block; margin-top: 12px; }
  .contact-head { position: absolute; left: 69px; top: 774px; font-size: 16px; }
  .contact-line { position: absolute; font-size: 15.5px; line-height: 17px; }
  .contact-line svg { position: absolute; left: -27px; }
  .weight-badge {
    position: absolute; left: 514px; top: 768px;
    width: 75px; height: 89px;
    border-radius: 16px;
    background: var(--tan);
    color: var(--tan-text);
  }
  .weight-badge .num { position: absolute; left: 11px; top: 10px; font-size: 48px; font-weight: 700; line-height: 48px; }
  .weight-badge .unit { position: absolute; right: 9px; top: 58px; font-size: 15px; }
</style>
</head>
<body>
  <section class="label">
    <div class="landscape" role="img" aria-label="Foto einer grünen Hügellandschaft der Eifel unter bewölktem Himmel"></div>
    <div class="hay-window" role="img" aria-label="Sichtfenster in Kaninchenform mit Blick auf Heu"></div>
    <div class="rabbits" role="img" aria-label="Foto mehrerer Kaninchen auf der Wiese"></div>
    <div class="brand-name">STROHKÖRBCHEN.DE</div>
    <div class="green-band"></div>

    <h2 class="benefits-title">Warum unser Heu bei unseren Kunden bzw.<br>Ihren kleinen Lieblingen so gut ankommt:</h2>
    <ul class="benefits">
      <li><svg viewBox="0 0 16 15"><path d="M1 8 L6 13 L15 1" fill="none" stroke="#1e1e1e" stroke-width="2.4"/></svg>enthält wenige Kräuter und wirkt sich positiv auf die<br>gesunde Ernährung aus</li>
      <li><svg viewBox="0 0 16 15"><path d="M1 8 L6 13 L15 1" fill="none" stroke="#1e1e1e" stroke-width="2.4"/></svg>lange Halme dienen der optimalen Unterstützung<br>des Zahnabriebs</li>
      <li><svg viewBox="0 0 16 15"><path d="M1 8 L6 13 L15 1" fill="none" stroke="#1e1e1e" stroke-width="2.4"/></svg>verbessert die Verdauung und daher gut verträglich<br>für Kleintiere</li>
      <li><svg viewBox="0 0 16 15"><path d="M1 8 L6 13 L15 1" fill="none" stroke="#1e1e1e" stroke-width="2.4"/></svg>als Streu angenehm wärmend</li>
      <li><svg viewBox="0 0 16 15"><path d="M1 8 L6 13 L15 1" fill="none" stroke="#1e1e1e" stroke-width="2.4"/></svg>frischer und aromatischer Heuduft</li>
      <li><svg viewBox="0 0 16 15"><path d="M1 8 L6 13 L15 1" fill="none" stroke="#1e1e1e" stroke-width="2.4"/></svg>nährstoffreiche, leckere, gesunde Gräser</li>
    </ul>

    <h2 class="analysis-title">HEU-FUTTERMITTELANALYSE</h2>
    <div class="analysis">
      <div class="analysis-cell" style="width:137px">Rohfaser<span class="value">31 %</span></div>
      <div class="analysis-cell" style="width:112px">Protein<span class="value">7,1 %</span></div>
      <div class="analysis-cell" style="width:135px">Fettgehalt<span class="value">1,6 %</span></div>
      <div class="analysis-cell" style="width:145px">Rohasche<span class="value">5,3 %</span></div>
    </div>

    <div class="contact-head">Kontakt</div>
    <div class="contact-line" style="left:70px;top:800px">
      <svg viewBox="0 0 12 16" width="12" height="16" style="top:9px"><path d="M6 1a5 5 0 0 0-5 5c0 4 5 9 5 9s5-5 5-9a5 5 0 0 0-5-5z" fill="#84c318"/><circle cx="6" cy="6" r="2" fill="#f5f1a9"/></svg>
      Strohkoerbchen.de, L. Brandner<br>Lindenweg 12 54321 Wiesental
    </div>
    <div class="contact-line" style="left:70px;top:842px">
      <svg viewBox="0 0 10 16" width="9" height="15" style="top:1px"><rect x="1" y="1" width="8" height="14" rx="1.5" fill="none" stroke="#84c318" stroke-width="2"/></svg>
      01234-5678
    </div>
    <div class="contact-line" style="left:344px;top:817px">
      <svg viewBox="0 0 14 10" width="13" height="9" style="top:5px;left:-26px"><rect width="14" height="10" fill="#84c318"/><path d="M0 0 L7 6 L14 0" fill="none" stroke="#f5f1a9" stroke-width="1.4"/></svg>
      mail@strohkoerbchen.de
    </div>
    <div class="contact-line" style="left:344px;top:840px">
      <svg viewBox="0 0 14 14" width="12" height="12" style="top:3px;left:-26px"><circle cx="7" cy="7" r="6" fill="none" stroke="#84c318" stroke-width="1.4"/><path d="M1 7h12M7 1v12M3 3.5h8M3 10.5h8" stroke="#84c318" stroke-width="1"/></svg>
      www.strohkörbchen.de
    </div>

    <div class="weight-badge"><span class="num">20</span><span class="unit">kg</span></div>
  </section>
</body>
</html>
```